Online Rug Store needs Clearance Banner

Website is: Lanternfield Carpets and Home
You can access it at: www.lanternfieldcarpetsandhome.com and login (top right) with password: trazok

*** update: When creating banners for my site, you have permission to use images from www.velbora.com, but ONLY for this project. The images/artwork are copyright allowable for use on www.lanternfieldcarpetsandhome.com projects.***

We need a home page banner sized 1000 wide x 500 tall pixels to promote a "Clearance Sale" on rugs. The banner can state:

1. Clearance Sale
2. Now in progress
3. Save an extra 20% with coupon code 'Mint20'
4. Ends March 31st
5. Plus Free Shipping and 30 day returns.

We prefer a banner that appears hand-drawn and artistic, not commercially produced. It is OK to use a room scene image, rug images, or just a colored/textured background with text and no images. Your choice.

Flat graphics with no shadows and 3-D effect preferred.
Attached is are 3 logo options, as well as an example banner with handcrafted, artistic styling that we prefer.

Target Market(s)

This should be an eye-catching banner to showcase a very urgent promotion. Consider using colors of red, white, gold, and black to make a strong statement on the home page.

Industry/Entity Type

Home And Garden

Requirements
Must have
• Winner must provide Photoshop editable file format (.psd format) including layers that can be edited.
Nice to have
• Hand-drawn, stenciled, scribbled, artistic graphics and fonts is nice because we sell rugs that are made by hand.
Should not have
• little to no shadowing. Avoid computerized graphics.

```html
<!DOCTYPE html>
<html lang="en">
<head>
<meta charset="utf-8">
<title>Clearance Sale Banner – Lanternfield Carpets and Home</title>
<link rel="stylesheet" href="https://fonts.googleapis.com/css2?family=Permanent+Marker&family=Kaushan+Script&family=Yellowtail&family=Poppins:wght@500&family=Roboto:wght@400&display=swap">
<style>
  :root {
    --rug-red: #7a0000;
    --pattern-red: #8e1d16;
    --pattern-deep: #6e0f0b;
    --gold: #e2b227;
    --white: #ffffff;
  }
  html, body {
    margin: 0;
    padding: 0;
    overflow: hidden;
    background: var(--white);
  }
  .banner {
    position: relative;
    width: 1200px;
    height: 600px;
    overflow: hidden;
  }
  .rug-pattern {
    position: absolute;
    inset: 0;
    background: linear-gradient(135deg, var(--pattern-red), var(--pattern-deep) 50%, var(--pattern-red));
  }
  .sale-panel {
    position: absolute;
    left: 102px;
    top: 102px;
    width: 1010px;
    height: 402px;
    background: var(--rug-red);
    color: var(--white);
  }
  .headline {
    position: absolute;
    left: 0;
    right: 0;
    top: 30px;
    margin: 0;
    text-align: center;
    font-weight: 400;
    white-space: nowrap;
  }
  .headline-caps {
    font-family: "Permanent Marker", cursive;
    font-size: 68px;
    letter-spacing: 12px;
    vertical-align: baseline;
  }
  .headline-script {
    font-family: "Kaushan Script", cursive;
    font-size: 112px;
    margin-left: 4px;
  }
  .status {
    position: absolute;
    left: 0;
    right: 0;
    top: 148px;
    margin: 0;
    text-align: center;
    font-weight: 400;
    white-space: nowrap;
  }
  .status-script {
    font-family: "Kaushan Script", cursive;
    font-size: 50px;
    margin-right: 14px;
  }
  .status-caps {
    font-family: "Permanent Marker", cursive;
    font-size: 40px;
    letter-spacing: 6px;
  }
  .offer {
    position: absolute;
    left: 0;
    right: 0;
    top: 248px;
    margin: 0;
    text-align: center;
    font-family: "Poppins", sans-serif;
    font-weight: 500;
    font-size: 20px;
    letter-spacing: 2.5px;
    white-space: nowrap;
  }
  .offer-amount {
    font-family: "Yellowtail", cursive;
    font-size: 34px;
    color: var(--gold);
    letter-spacing: 2px;
    margin: 0 6px;
  }
  .coupon-code {
    font-family: "Permanent Marker", cursive;
    font-size: 28px;
    color: var(--gold);
    letter-spacing: 3px;
    margin-left: 6px;
  }
  .perks, .deadline {
    position: absolute;
    top: 350px;
    margin: 0;
    font-family: "Roboto", sans-serif;
    font-size: 26px;
    white-space: nowrap;
  }
  .perks { left: 17px; }
  .deadline { right: 22px; }
  .highlight { color: var(--gold); }
</style>
</head>
<body>
  <main class="banner">
    <div class="rug-pattern" role="img" aria-label="Red, gold and black diamond rug pattern background"></div>
    <section class="sale-panel">
      <h1 class="headline"><span class="headline-caps">CLEARANCE</span><span class="headline-script">Sale</span></h1>
      <h2 class="status"><span class="status-script">Now</span><span class="status-caps">IN PROGRESS</span></h2>
      <p class="offer">Save an <span class="offer-amount">extra 20%</span> with coupon code <span class="coupon-code">'MINT20'</span></p>
      <p class="perks">Plus <span class="highlight">FREE SHIPPING</span> and <span class="highlight">30 DAY RETURNS</span></p>
      <p class="deadline">Ends March 31st</p>
    </section>
  </main>
</body>
</html>
```